Quarrow financial services, is a financial company that provides consultancy, brokerage services, and funding.

we will be providing the clients with insights, knowledge and data with regards to the financial markets.

with the brokerage services we will try to find the suitable counterparts that provide them with the best investments that suits their needs and expected return.

Target Market(s)

financial institutions, Corporates, high-net worth individuals

Industry/Entity Type

Financial Service

Contact Information for Business Card

Font styles to use
Other font styles liked:
• applemyungjo

Colors
00a990
848484

Requirements
Must have
• the logo at the back
Nice to have
• Finesse
Should not have
• boldness

```html
<!DOCTYPE html>
<html lang="en">
<head>
<meta charset="utf-8">
<title>Quarrow Financial Services — Business Card</title>
<link rel="stylesheet" href="https://fonts.googleapis.com/css2?family=Cormorant+Garamond:wght@500&family=Open+Sans:ital,wght@0,400;0,600;1,400&display=swap">
<style>
  :root {
    --backdrop: #4a4a4a;
    --card-white: #ffffff;
    --brand-green: #7a9b4b;
    --brand-slate: #3f4a52;
    --text-grey: #555b60;
    --mark-tint: #c9d4bd;
    --rule-grey: #d6d6d6;
  }
  * { box-sizing: border-box; margin: 0; padding: 0; }
  html, body {
    width: 1105px; height: 1200px; overflow: hidden;
    background: var(--backdrop);
    font-family: "Open Sans", Arial, sans-serif;
  }
  .card {
    position: absolute; left: 196px; width: 720px; height: 413px;
    overflow: hidden;
  }
  .card-front { top: 145px; background: var(--card-white); }
  .card-back { top: 602px; background: var(--brand-green); }

  .lockup { position: absolute; text-align: center; }
  .lockup .mark { display: block; width: 64px; height: 80px; margin: 0 auto; }
  .lockup .brand-name {
    font-family: "Cormorant Garamond", Georgia, serif;
    font-weight: 500; font-size: 30px; line-height: 1.05;
    letter-spacing: 1px; margin-top: 22px;
  }
  .lockup .tagline {
    font-family: "Cormorant Garamond", Georgia, serif;
    font-weight: 500; font-size: 11px; letter-spacing: 0.5px; margin-top: 6px;
    text-transform: uppercase;
  }
  .card-front .lockup { left: 40px; top: 78px; width: 300px; color: var(--brand-slate); }
  .card-front .mark { background: var(--mark-tint); }
  .card-back .lockup { left: 210px; top: 95px; width: 300px; color: #ffffff; }
  .card-back .mark { background: #dfe6d6; }

  .divider {
    position: absolute; left: 369px; top: 82px; width: 1px; height: 220px;
    background: var(--rule-grey);
  }
  .contact { position: absolute; left: 408px; top: 90px; color: var(--text-grey); font-size: 19px; line-height: 1.35; }
  .contact .person-name { color: var(--brand-green); font-weight: 600; font-size: 25px; letter-spacing: 0.5px; }
  .contact .role { margin-bottom: 24px; }
  .contact .row { display: flex; align-items: center; gap: 10px; }
  .contact .row svg { width: 16px; height: 16px; fill: var(--brand-green); flex: none; }

  .front-band { position: absolute; left: 0; top: 361px; width: 720px; height: 33px; display: flex; }
  .front-band .band-green {
    width: 580px; background: var(--brand-green); color: #fff;
    font-size: 18px; letter-spacing: 5px; line-height: 33px; padding-left: 150px;
  }
  .front-band .band-slate { flex: 1; background: var(--brand-slate); position: relative; }
  .front-band .band-slate .marker {
    position: absolute; left: 12px; top: -14px; width: 26px; height: 40px; background: var(--mark-tint);
  }

  .back-web {
    position: absolute; left: 0; width: 720px; top: 352px; text-align: center;
    color: #fff; font-style: italic; font-size: 19px; letter-spacing: 1.5px;
  }
</style>
</head>
<body>
  <section class="card card-front">
    <div class="lockup">
      <span class="mark"></span>
      <div class="brand-name">Quarrow financial services</div>
      <div class="tagline">Your financial prosperity is our concern</div>
    </div>
    <div class="divider"></div>
    <div class="contact">
      <div class="person-name">DANIEL HART</div>
      <div class="role">CEO/Founder</div>
      <div>4120 Willowmere Road</div>
      <div>Fairbanks, Alaska 99701</div>
      <div class="row">
        <svg viewBox="0 0 24 24" aria-hidden="true"><path d="M6.6 10.8a15.1 15.1 0 0 0 6.6 6.6l2.2-2.2a1 1 0 0 1 1-.25 11.4 11.4 0 0 0 3.6.57 1 1 0 0 1 1 1V20a1 1 0 0 1-1 1A17 17 0 0 1 3 4a1 1 0 0 1 1-1h3.5a1 1 0 0 1 1 1c0 1.25.2 2.45.57 3.57a1 1 0 0 1-.25 1z"/></svg>
        <span>907 555 0184</span>
      </div>
      <div class="row">
        <svg viewBox="0 0 24 24" aria-hidden="true"><path d="M2 5h20v14H2z M2 5l10 8 10-8" /></svg>
        <span>hello@quarrowmail.com</span>
      </div>
    </div>
    <div class="front-band">
      <div class="band-green">www.quarrow.com</div>
      <div class="band-slate"><span class="marker"></span></div>
    </div>
  </section>

  <section class="card card-back">
    <div class="lockup">
      <span class="mark"></span>
      <div class="brand-name">Quarrow financial services</div>
      <div class="tagline">Your financial prosperity is our concern</div>
    </div>
    <div class="back-web">www.quarrowfinancial.com</div>
  </section>
</body>
</html>
```